Tri-Fold Menu of Services for our Eyelash and Skin Care Spa

We need a beautiful spa service menu for our upscale spa in St. Charles Missouri. We specialize in providing treatments that are specific to the clients needs. Our services are eyelash extensions, skin care treatments, full body waxing and makeup application. Our spa colors are dark purples and greys and we are not opposed to additional colors that would complement those colors. We do a lot of eyelash extensions and while we do what those services listed we would like the skin care treatments to be in an area that would be noticed first. One of the attachments lists all of our services, descriptions and prices (please be sure to include all services and pricing. descriptions if possible). And our website has more information about us if needed. The website was not professionally done. So it DOESN'T represent our style exactly.

I HAVE ATTACHED A FEW PHOTOS BUT THEY DON'T HAVE TO BE USED.

Target Market(s)

women who would like to look their best, 35-55, annual income of 100,000+, she is usually busy and her children (if she has any) are high school age or older.

Industry/Entity Type

It Service

Font styles to use
Serif
Sans Serif

Requirements
Must have
• Must list all of our services. If it works to have the descriptions that would be great.
Nice to have
• If it works to have the descriptions of each service that would be great.

```html
<!DOCTYPE html>
<html lang="en">
<head>
<meta charset="utf-8">
<title>Velora Lash &amp; Skin Spa – Service Menu</title>
<link href="https://fonts.googleapis.com/css2?family=Roboto+Condensed:wght@400;700&family=Open+Sans:wght@400&display=swap" rel="stylesheet">
<style>
  :root{
    --canvas:#e8e6e3;
    --paper:#ffffff;
    --ink:#1e1e1e;
    --brand-purple:#3b1840;
    --spa-red:#b8141d;
    --spa-red-dark:#8c0d14;
    --swoosh-grey:#a9aaae;
    --skin-light:#f1d9cb;
    --skin-mid:#d9a98f;
    --towel:#c9b7a6;
  }
  html,body{margin:0;padding:0;width:1200px;height:1200px;overflow:hidden;background:var(--canvas);}
  .brochure{
    position:absolute;left:40px;top:168px;width:1120px;height:863px;
    background:var(--paper);box-shadow:0 4px 14px rgba(0,0,0,.25);overflow:hidden;
    font-family:"Roboto Condensed",sans-serif;color:var(--ink);
  }
  .photo{position:absolute;}
  .photo--facial-device{left:0;top:0;width:370px;height:205px;
    background:linear-gradient(135deg,#cfc3b8 0%,var(--skin-light) 45%,#e7e3df 100%);}
  .photo--powder-brush{left:370px;top:0;width:375px;height:300px;
    background:radial-gradient(ellipse at 70% 30%,var(--skin-light) 0%,#f6e7de 45%,#ffffff 80%);}
  .photo--face-massage{left:745px;top:400px;width:375px;height:463px;
    background:linear-gradient(160deg,#7a4a36 0%,var(--skin-mid) 30%,var(--skin-light) 60%,#f4efea 100%);}
  .shapes{position:absolute;left:0;top:0;width:1120px;height:863px;}

  .menu{position:absolute;left:16px;top:243px;width:338px;font-size:13.6px;line-height:22.4px;}
  .menu__heading{text-align:center;font-weight:700;font-size:14px;}
  .row{display:flex;align-items:baseline;white-space:nowrap;}
  .leader{flex:1;border-bottom:1.5px dotted #444;margin:0 2px;transform:translateY(-3px);}
  .lash-head{display:flex;justify-content:flex-end;font-weight:700;font-size:14px;}
  .lash-head span{width:78px;text-align:center;}
  .lash-head span:last-child{width:64px;text-align:right;}
  .row--lash .name{width:105px;}
  .menu__note{font-size:13px;line-height:18.6px;text-align:justify;margin-top:2px;}

  .map-label{position:absolute;left:375px;top:406px;width:370px;text-align:center;
    font-weight:700;font-size:42px;}
  .brand{position:absolute;text-align:center;color:var(--brand-purple);
    font-family:"Open Sans",sans-serif;font-weight:400;line-height:1;}
  .brand__name{display:block;font-size:56px;letter-spacing:1px;}
  .brand__tag{display:block;font-size:17px;margin-top:4px;}
  .brand--center{left:375px;top:588px;width:370px;}
  .brand--cover{left:800px;top:262px;width:270px;}
  .brand--cover .brand__name{font-size:50px;}
  .contact{position:absolute;left:375px;top:716px;width:370px;text-align:center;
    font-family:"Open Sans",sans-serif;font-size:32px;line-height:45px;}
  .slogan{position:absolute;left:745px;top:30px;width:375px;text-align:center;color:#fff;
    font-family:"Open Sans",sans-serif;font-size:32px;line-height:43px;}
</style>
</head>
<body>
<div class="brochure">
  <div class="photo photo--facial-device" role="img" aria-label="Photo of a woman receiving a facial skin treatment with a device"></div>
  <div class="photo photo--powder-brush" role="img" aria-label="Photo of a woman with closed eyes having powder applied with a makeup brush"></div>
  <div class="photo photo--face-massage" role="img" aria-label="Photo of a woman relaxing during a face and temple massage"></div>

  <svg class="shapes" viewBox="0 0 1370 1056" preserveAspectRatio="none" aria-hidden="true">
    <defs>
      <linearGradient id="redPanel" x1="0" y1="0" x2="1" y2="1">
        <stop offset="0" stop-color="#c8161f"/>
        <stop offset="1" stop-color="#8c0d14"/>
      </linearGradient>
    </defs>
    <!-- white swoosh over the left and centre panels -->
    <path d="M0,282 Q460,210 912,330 L912,1056 L0,1056 Z" fill="#fff"/>
    <path d="M0,278 Q460,205 912,325 L940,335 Q480,225 0,284 Z" fill="var(--swoosh-grey)"/>
    <path d="M0,268 Q470,190 912,310" fill="none" stroke="#d7d8da" stroke-width="3"/>
    <!-- cover panel -->
    <path d="M912,0 L1370,0 L1370,520 L912,300 Z" fill="url(#redPanel)"/>
    <path d="M1230,505 L1370,575 L1370,610 L1210,530 Z" fill="var(--swoosh-grey)"/>
    <circle cx="1140" cy="368" r="187" fill="#fff"/>
    <rect x="912" y="300" width="140" height="190" fill="#fff" opacity="0"/>
  </svg>

  <div class="menu">
    <div class="menu__heading">EYELASHES</div>
    <div class="lash-head"><span>Full Set</span><span>Demi Set</span><span>Touch up</span></div>
    <div class="row row--lash"><span>Classic</span><span class="leader"></span><span>175</span><span class="leader"></span><span>110</span><span class="leader"></span><span>60</span></div>
    <div class="row row--lash"><span>Volume Technique</span><span class="leader"></span><span>220</span><span class="leader"></span><span>135</span><span class="leader"></span><span>72</span></div>
    <div class="menu__heading">WAXING</div>
    <div class="row"><span>Eyebrows</span><span class="leader"></span><span>$17</span></div>
    <div class="row"><span>Upper Lip</span><span class="leader"></span><span>$14</span></div>
    <div class="row"><span>Chin</span><span class="leader"></span><span>$14</span></div>
    <div class="row"><span>Sides of face</span><span class="leader"></span><span>$14</span></div>
    <div class="row"><span>Bikini</span><span class="leader"></span><span>$27+</span></div>
    <div class="row"><span>Brazilian</span><span class="leader"></span><span>$55+</span></div>
    <div class="row"><span>Underarm</span><span class="leader"></span><span>$22</span></div>
    <div class="row"><span>Arms</span><span class="leader"></span><span>Full $35</span><span class="leader"></span><span>Lower $26</span></div>
    <div class="row"><span>Legs</span><span class="leader"></span><span>Full $62</span><span class="leader"></span><span>Lower $40</span></div>
    <div class="row"><span>Chest</span><span class="leader"></span><span>$44</span></div>
    <div class="row"><span>Back</span><span class="leader"></span><span>$44</span></div>
    <div class="menu__heading">TINTING</div>
    <div class="row"><span>Eyebrows</span><span class="leader"></span><span>$20</span></div>
    <div class="row"><span>Eyelashes</span><span class="leader"></span><span>$20</span></div>
    <div class="row"><span>both</span><span class="leader"></span><span>$30</span></div>
    <div class="row"><span>Neck, Back &amp; Head Massage 30 min.</span><span class="leader"></span><span>$45</span></div>
    <div class="row"><span>Aromatherapy Scalp Massage 10 min.</span><span class="leader"></span><span>$15</span></div>
    <div class="row"><span>Foot Massage and Scrub 15 min.</span><span class="leader"></span><span>$20</span></div>
    <div class="row"><span>Headache &amp; Migraine Relief Treatment 30 min.</span><span class="leader"></span><span>$45</span></div>
    <p class="menu__note">Relief from headaches caused by stress, tension, hormonal imbalances or sensitivities using cold stones and massaging techniques for the face.</p>
  </div>

  <div class="map-label">map here</div>

  <div class="brand brand--center"><span class="brand__name">Velora</span><span class="brand__tag">Lash &amp; Skin Spa</span></div>

  <div class="contact">put your<br>address and<br>contact info here</div>

  <div class="slogan">put your<br>slogan here</div>

  <div class="brand brand--cover"><span class="brand__name">Velora</span><span class="brand__tag">Lash &amp; Skin Spa</span></div>
</div>
</body>
</html>
```